BrightPath Medical Exercise, LLC specializes in post rehab medical exercise for clients who have been discharged from physical therapy and/or other medical services and are in need of continued cardiovascular, strength, flexibility, endurance training and management of their medical conditions. We strive to bridge the gap between healthcare and fitness by staying in communication with the referring physician and /or physical therapist with updated progress notes to follow each clients progression, making sure each client is appropriate for exercise and identifying any red flags throughout the initial assessment and screening of the client, and referring those clients back to the physician and/or therapist when necessary.
Colors
Designer to choose colors to be used in the design.
Requirements
Must have
- Pictures of a trainer working with a client one on one during exercise, and group exercise
Nice to have
- Pictures that portray the bridge between healthcare and fitness
Should not have
- Cursive writing

```html
<!DOCTYPE html>
<html lang="en">
<head>
<meta charset="utf-8">
<title>BrightPath Medical Exercise – Rack Card</title>
<link href="https://fonts.googleapis.com/css2?family=Arvo:ital,wght@1,700&family=Lato:ital,wght@0,300;0,700;0,900;1,300;1,700;1,900&display=swap" rel="stylesheet">
<style>
  :root {
    --page: #e4e4e6;
    --paper: #f0eee8;
    --ink: #1d2538;
    --red: #e0524a;
    --body: #3a3d44;
    --wood-light: #b9a488;
    --wood-dark: #4a4237;
    --white: #ffffff;
  }
  * { box-sizing: border-box; margin: 0; padding: 0; }
  html, body { width: 1200px; height: 1200px; overflow: hidden; }
  body {
    background: var(--page);
    font-family: "Lato", sans-serif;
    color: var(--body);
    position: relative;
  }
  .rack-card {
    position: absolute;
    left: 320px; top: 40px;
    width: 560px; height: 1120px;
    background: var(--paper);
    overflow: hidden;
  }
  .hero-photo {
    position: absolute; left: 0; top: 0;
    width: 100%; height: 280px;
    background: linear-gradient(180deg, var(--wood-dark) 0%, #5d5345 35%, var(--wood-light) 60%, #d8cdbd 85%, var(--paper) 100%);
  }
  .brand {
    position: absolute; left: 22px; top: 300px;
    width: 160px;
    display: flex; flex-direction: column; align-items: center; gap: 10px;
  }
  .brand-dot {
    width: 80px; height: 80px; border-radius: 50%;
    background: var(--red);
  }
  .brand-name {
    font-weight: 900; font-size: 13px; line-height: 1.2;
    color: var(--ink); text-align: center; text-transform: uppercase;
  }
  .headline {
    position: absolute; left: 188px; top: 292px; width: 360px;
    font-family: "Arvo", serif; font-style: italic; font-weight: 700;
    font-size: 27px; line-height: 32px; text-align: center;
    color: var(--ink); text-transform: uppercase;
  }
  .section-title {
    position: absolute; left: 0; width: 100%;
    padding-left: 34px;
    font-weight: 900; font-size: 19px; line-height: 24px;
    color: var(--red); text-transform: uppercase;
  }
  .services-title { top: 455px; }
  .services {
    position: absolute; left: 30px; top: 492px; list-style: none;
    font-style: italic; font-weight: 300; font-size: 15px; line-height: 21px;
  }
  .services li { display: flex; align-items: center; gap: 5px; }
  .services svg { width: 13px; height: 11px; flex: none; }
  .conditions-title { top: 577px; }
  .conditions {
    position: absolute; top: 647px; list-style: none;
    font-style: italic; font-weight: 300; font-size: 16px; line-height: 22.5px;
  }
  .conditions li { position: relative; padding-left: 22px; }
  .conditions li::before {
    content: ""; position: absolute; left: 3px; top: 8px;
    width: 8px; height: 8px; border-radius: 50%; background: var(--red);
  }
  .conditions-left { left: 30px; }
  .conditions-right { left: 290px; }
  .quote-band {
    position: absolute; left: 0; bottom: 0;
    width: 100%; height: 132px;
    background: var(--red); color: var(--white);
    text-align: center; padding-top: 16px;
  }
  .quote-text {
    font-weight: 900; font-style: italic; font-size: 22px; line-height: 29px;
  }
  .quote-author {
    font-weight: 300; font-style: italic; font-size: 19px; margin-top: 3px;
  }
  .quote-mark {
    position: absolute; font-family: "Arvo", serif; font-style: normal;
    font-weight: 700; font-size: 64px; line-height: 1;
  }
  .quote-open { left: 40px; top: 14px; }
  .quote-close { right: 46px; top: 44px; }
</style>
</head>
<body>
  <article class="rack-card">
    <div class="hero-photo" role="img" aria-label="Photo of blue hand weights and a water bottle on a wooden deck"></div>

    <div class="brand">
      <span class="brand-dot"></span>
      <span class="brand-name">BrightPath<br>Medical Exercise</span>
    </div>

    <h1 class="headline">Getting you back to function as quickly and safely as possible</h1>

    <h2 class="section-title services-title">Our products and services:</h2>
    <ul class="services">
      <li><svg viewBox="0 0 13 11"><path d="M1 6l4 4 7-9" fill="none" stroke="#e0524a" stroke-width="2.4"/></svg>Initial Assessment and Functional Screening</li>
      <li><svg viewBox="0 0 13 11"><path d="M1 6l4 4 7-9" fill="none" stroke="#e0524a" stroke-width="2.4"/></svg>One-On-One supervised post rehab exercise</li>
      <li><svg viewBox="0 0 13 11"><path d="M1 6l4 4 7-9" fill="none" stroke="#e0524a" stroke-width="2.4"/></svg>Online consultation with individualized home exercise program</li>
    </ul>

    <h2 class="section-title conditions-title">We offer management of the<br>following conditions and more:</h2>
    <ul class="conditions conditions-left">
      <li>Diabetes</li>
      <li>Hypertension</li>
      <li>ACL Rupture</li>
      <li>Ankle Fracture</li>
      <li>Bicipital Tendonitis</li>
      <li>Total Hip Replacement</li>
      <li>Total Knee Replacement</li>
      <li>Spinal Stenosis</li>
      <li>Multiple Sclerosis</li>
      <li>Shoulder Dislocation</li>
      <li>Scoliosis</li>
      <li>Osteoporosis</li>
      <li>Osteoarthritis</li>
      <li>Cervical disc herniation</li>
    </ul>
    <ul class="conditions conditions-right">
      <li>AC Joint Separation</li>
      <li>Fibromyalgia</li>
      <li>Spondylothesis</li>
      <li>Parkinson’s Disease</li>
      <li>Tibial Plateau Fracture</li>
      <li>Tennis Elbow/Golfer’s Elbow</li>
      <li>Carpal Tunnel Syndrome</li>
      <li>Total Shoulder Replacement</li>
      <li>Bicipital Tendonitis</li>
      <li>Patello-Femoral Syndrome</li>
      <li>Rotator Cuff Syndrome</li>
      <li>Cervical Strain</li>
      <li>Impingement Syndrome</li>
      <li>Laminectomy</li>
    </ul>

    <footer class="quote-band">
      <span class="quote-mark quote-open">“</span>
      <p class="quote-text">Exercise is the key to long-term<br>management of most medical conditions</p>
      <p class="quote-author">~ Daniel R Hayes, PhD, PT</p>
      <span class="quote-mark quote-close">”</span>
    </footer>
  </article>
</body>
</html>
```